Business Card for Marriage Commissioner

I am a marriage commissioner in the province of Alberta, meaning that I perform civil unions here. I have been trying to think of a unique design for my business card, something a bit different. A lot of "unique" designs seem to incorporate unique cuts or "some assembly required" or printed on plastic or meat. I would like my design to be a full colour card that is a typical business card size.

The information on the card should have:
Lou Varnik
my occupation: Marriage Commissioner
my website: www.louvarnik.ca
my e-mail: lou@louvarnik.ca
my phone: 780-418-2964

I originally submitted a design to the printer that had a screen capture of a findly search window, with my name and occupation in the text box. And underneath that, my phone number. Nothing else. They indicated they could not print this because it was a copyright violation.

One option on the design is I am a retired chemist-so a chemistry themed card would also be of interest, as long as it isn't a "Rusted Tide" theme, as I have that on my other business cards already...

I would prefer a single sided card, but I am open to a double sided card if it is clever!

I would also prefer not to have pictures of male and female couples as in my position I will also marry same sex couples. Same thing for male/female symbols. Someone has submitted two graduated cylinders in love, which is very clever, and gets around this male/female type.

Thanks for your help and interest.

Target Market(s)

Young couples.

Industry/Entity Type

Plastic

Requirements
Nice to have
• chemistry ideas!
Should not have
• Male/female pictures, male/female symbols.
No QR codes.
No transparent designs, will go on paper stock.

```html
<!DOCTYPE html>
<html lang="en">
<head>
<meta charset="utf-8">
<title>Lou Varnik – Marriage Commissioner</title>
<link rel="stylesheet" href="https://fonts.googleapis.com/css2?family=Open+Sans:wght@400;600;700&family=Parisienne&display=swap">
<style>
  :root {
    --page-bg: #e9e6e1;
    --card-bg: #ffffff;
    --brown: #5c4530;
    --brown-dark: #4a3624;
    --brown-light: #6e543b;
    --ink: #3a2c20;
    --rule: #b9ada0;
    --rule-light: #d9d4ce;
    --ornament: #d6d6da;
    --ornament-soft: #ececef;
    --photo-warm: #d9b79c;
    --photo-soft: #f2e6dc;
  }
  * { box-sizing: border-box; margin: 0; padding: 0; }
  html, body {
    width: 1200px; height: 940px; overflow: hidden;
    background: var(--page-bg);
  }
  .card {
    position: absolute; left: 100px; top: 185px;
    width: 1000px; height: 570px;
    background: var(--card-bg);
    box-shadow: 0 10px 30px rgba(0,0,0,.18);
  }
  .banner {
    position: absolute; left: 30px; top: 40px;
    width: 940px; height: 190px;
    background: linear-gradient(135deg, var(--brown-light), var(--brown) 45%, var(--brown-dark));
  }
  .banner__photo {
    position: absolute; left: 0; top: 0;
    width: 300px; height: 190px;
    border-radius: 0 95px 95px 0;
    background: radial-gradient(circle at 65% 45%, var(--photo-soft), var(--photo-warm) 55%, #8a6a52);
  }
  .banner__quote {
    position: absolute; left: 400px; top: 34px;
    font-family: "Parisienne", cursive;
    color: #fff; font-size: 46px; line-height: 1.15;
  }
  .banner__quote span { display: block; padding-left: 50px; }
  .banner-rule {
    position: absolute; left: 330px; top: 248px;
    width: 640px; height: 1px; background: var(--rule-light);
  }
  .identity { position: absolute; left: 50px; top: 250px; }
  .identity__name {
    font-family: "Open Sans", sans-serif; font-weight: 700;
    font-size: 52px; color: var(--brown); letter-spacing: -0.5px; line-height: 1.1;
  }
  .identity__role {
    font-family: "Open Sans", sans-serif; font-weight: 600;
    font-size: 18px; color: var(--ink); margin-top: -2px;
  }
  .contacts { position: absolute; left: 50px; top: 355px; width: 430px; list-style: none; }
  .contacts__item {
    display: flex; align-items: center; gap: 10px;
    height: 56px; border-bottom: 1.5px solid var(--rule);
    font-family: "Open Sans", sans-serif; font-size: 28px; color: var(--ink);
  }
  .contacts__icon { width: 32px; height: 32px; flex: none; }
  .divider {
    position: absolute; left: 530px; top: 290px;
    width: 1px; height: 230px; background: var(--rule-light);
  }
  .ornament {
    position: absolute; left: 580px; top: 280px;
    width: 390px; height: 210px; border-radius: 105px 105px 105px 18px;
    background: linear-gradient(160deg, var(--ornament-soft) 0%, var(--ornament) 55%, var(--ornament-soft) 100%);
  }
  .butterfly {
    position: absolute; left: 548px; top: 420px;
    width: 96px; height: 90px; border-radius: 50% 50% 45% 45%;
    background: linear-gradient(180deg, var(--ornament), var(--ornament-soft));
  }
  .foot-rule {
    position: absolute; left: 560px; top: 535px;
    width: 400px; height: 1px; background: var(--rule-light);
  }
</style>
</head>
<body>
  <main class="card">
    <section class="banner">
      <div class="banner__photo" role="img" aria-label="Portrait photo of a wedding couple"></div>
      <p class="banner__quote">Love builds bridges<span>where there are none.</span></p>
    </section>
    <div class="banner-rule"></div>

    <header class="identity">
      <h1 class="identity__name">Lou Varnik</h1>
      <p class="identity__role">Marriage Commissioner</p>
    </header>

    <ul class="contacts">
      <li class="contacts__item">
        <svg class="contacts__icon" viewBox="0 0 32 32" aria-hidden="true">
          <rect width="32" height="32" rx="3" fill="var(--brown)"/>
          <path d="M8 13c0-3 4-5 8-5s8 2 8 5l-3 1-1-2c-2-1-6-1-8 0l-1 2z" fill="#fff"/>
          <rect x="10" y="16" width="12" height="8" rx="2" fill="#fff"/>
        </svg>
        780-418-2964
      </li>
      <li class="contacts__item">
        <svg class="contacts__icon" viewBox="0 0 32 32" aria-hidden="true">
          <rect width="32" height="32" rx="3" fill="var(--brown)"/>
          <rect x="7" y="10" width="18" height="12" fill="none" stroke="#fff" stroke-width="2"/>
          <path d="M7 10l9 7 9-7" fill="none" stroke="#fff" stroke-width="2"/>
        </svg>
        www.louvarnik.ca
      </li>
      <li class="contacts__item">
        <svg class="contacts__icon" viewBox="0 0 32 32" aria-hidden="true">
          <rect width="32" height="32" rx="3" fill="var(--brown)"/>
          <circle cx="16" cy="16" r="9" fill="none" stroke="#fff" stroke-width="2"/>
          <circle cx="16" cy="16" r="3.5" fill="none" stroke="#fff" stroke-width="2"/>
        </svg>
        lou@louvarnik.ca
      </li>
    </ul>

    <div class="divider"></div>
    <div class="ornament" role="img" aria-label="Light grey floral swirl ornament with small snowflakes"></div>
    <div class="butterfly" role="img" aria-label="Light grey butterfly illustration"></div>
    <div class="foot-rule"></div>
  </main>
</body>
</html>
```